Retail Jewelry Business Card Design Project

We are in need of a new business card design for a retail jewelry store. This store is in the business of fine jewelry including but not specific to bridal jewelry, diamonds, designer jewelry and watches.

This store has been in business for 20 years but continues to strive for a modern professional appeal. The main colors use for this business are a royal blue, white and silver.

Target Market(s)

Target market is ages 18-50

Industry/Entity Type

Jewelry

Requirements
Must have
• Sales Person Name
Sales Person Email Address

Store Address
Store Phone
Website

Standard business card size. No odd shapes or sizes.
Nice to have
• Overall modern feel for card.

We have thought that a design with a nice feature of the logo on the back of the card would be nice but open to ideas.
Should not have
• No specific images of jewelry should be used.

```html
<!DOCTYPE html>
<html lang="en">
<head>
<meta charset="utf-8">
<title>Martin Hale Fine Jewelry – Business Card</title>
<link rel="stylesheet" href="https://fonts.googleapis.com/css2?family=Lato:wght@400;700&display=swap">
<style>
  :root {
    --royal: #3b38a6;
    --royal-deep: #2f2c92;
    --royal-glow: #5a57bd;
    --white: #ffffff;
    --silver: #c9cbd6;
    --silver-dark: #8c8fa0;
    --ink-grey: #6d6d78;
    --page: #ecebe8;
  }
  * { box-sizing: border-box; margin: 0; padding: 0; }
  html, body {
    width: 1200px; height: 990px; overflow: hidden;
    background: var(--page);
    font-family: "Lato", "Helvetica Neue", Arial, sans-serif;
  }
  .canvas { position: relative; width: 1200px; height: 990px; }
  .card {
    position: absolute; left: 250px; width: 700px; height: 400px;
    background: var(--royal); overflow: hidden;
    box-shadow: 0 6px 18px rgba(0,0,0,.18);
  }
  .card--front { top: 65px; }
  .card--back { top: 525px; }
  .card__art { position: absolute; inset: 0; }

  .wordmark {
    position: absolute; text-align: center;
    color: var(--white); font-weight: 400; line-height: 1;
  }
  .wordmark__name { display: block; }
  .wordmark__rule {
    display: block; height: 2px; background: var(--white);
    margin: 10px auto 8px;
  }
  .wordmark__sub { display: block; font-size: .46em; letter-spacing: .22em; line-height: 1; }

  .card--front .wordmark { top: 58px; left: 20px; width: 640px; font-size: 44px; }
  .card--front .wordmark__rule { width: 380px; }
  .card--back .wordmark { top: 138px; left: 0; width: 700px; font-size: 54px; }
  .card--back .wordmark__rule { width: 400px; margin: 12px auto 10px; }

  .store-info {
    position: absolute; left: 46px; top: 222px; width: 290px;
    color: var(--white); font-size: 18px; line-height: 27px; text-align: center;
    font-style: normal;
  }
  .contact { position: absolute; left: 375px; top: 220px; width: 300px; }
  .contact__name { color: var(--royal); font-size: 20px; font-weight: 700; }
  .contact__phone {
    margin-top: 50px; color: var(--ink-grey); font-size: 17px;
    display: flex; align-items: center; gap: 10px;
  }
  .contact__phone-mark { width: 8px; height: 22px; background: var(--silver); }
  .email {
    position: absolute; left: 22px; top: 350px;
    color: var(--royal); font-size: 18px;
  }
</style>
</head>
<body>
<main class="canvas">

  <section class="card card--front" aria-label="Business card front">
    <svg class="card__art" width="700" height="400" viewBox="0 0 700 400" aria-hidden="true">
      <defs>
        <linearGradient id="silverSheen" x1="0" x2="1">
          <stop offset="0" stop-color="#ffffff"/>
          <stop offset="1" stop-color="#c9cbd6"/>
        </linearGradient>
      </defs>
      <circle cx="330" cy="150" r="215" fill="var(--royal-glow)" opacity=".45"/>
      <rect x="14" y="12" width="672" height="170" fill="none" stroke="var(--white)" stroke-width="1.5"/>
      <path d="M0 205 Q0 195 20 195 L40 195 Q20 200 20 225 L20 335 L0 335 Z" fill="var(--white)"/>
      <path d="M345 335 L345 215 Q345 198 365 198 L700 198 L700 335 Z" fill="var(--white)"/>
      <path d="M640 198 Q700 260 560 335 L700 335 L700 198 Z" fill="var(--royal)"/>
      <rect x="0" y="335" width="700" height="65" fill="url(#silverSheen)"/>
      <rect x="22" y="382" width="300" height="4" fill="var(--royal)"/>
    </svg>

    <p class="wordmark">
      <span class="wordmark__name">Martin Hale</span>
      <span class="wordmark__rule"></span>
      <span class="wordmark__sub">FINE JEWELRY</span>
    </p>

    <address class="store-info">
      Martin Hale Fine Jewelry<br>
      2280 Linden Avenue<br>
      Bay Harbor, FL 32450<br>
      www.martinhalejewelry.com
    </address>

    <div class="contact">
      <p class="contact__name">Martin Hale Corwin</p>
      <p class="contact__phone"><span class="contact__phone-mark"></span>T: (555) 218-0473</p>
    </div>

    <p class="email">martin@martinhalejewelry.com</p>
  </section>

  <section class="card card--back" aria-label="Business card back">
    <svg class="card__art" width="700" height="400" viewBox="0 0 700 400" aria-hidden="true">
      <defs>
        <linearGradient id="edgeSheen" x1="0" x2="1">
          <stop offset="0" stop-color="#ffffff" stop-opacity="0"/>
          <stop offset=".5" stop-color="#ffffff" stop-opacity=".9"/>
          <stop offset="1" stop-color="#ffffff" stop-opacity="0"/>
        </linearGradient>
      </defs>
      <circle cx="350" cy="200" r="240" fill="var(--royal-glow)" opacity=".45"/>
      <rect x="16" y="16" width="668" height="368" fill="none" stroke="var(--white)" stroke-width="1.5"/>
      <rect x="180" y="6" width="340" height="5" fill="url(#edgeSheen)"/>
      <rect x="180" y="389" width="340" height="5" fill="url(#edgeSheen)"/>
    </svg>

    <p class="wordmark">
      <span class="wordmark__name">Martin Hale</span>
      <span class="wordmark__rule"></span>
      <span class="wordmark__sub">FINE JEWELRY</span>
    </p>
  </section>

</main>
</body>
</html>
```